Revelation Sanctuary Flyer

We need a flyer for a church seminar that focuses on the Revelation and the sanctuary, it will show images with giants, UFOs maybe some pyramids, sanctuary furniture pieces.

Front Cover, Middle and Back cover. size 8.5 x 11 folded in the middle
The information is in file 1 and file 2.
The other files are examples and ideas for layout.

Target Market(s)

Churches

Requirements
Must have
• 1. Flyer design files have to be print ready.
• 2. Must have appropriate bleed size and safe zone
• PDF, JPEG, PSD, AI, TIFF
Nice to have
• Images of Giants, UFO, Sanctuary building, Pyramids

```html
<!DOCTYPE html>
<html lang="en">
<head>
<meta charset="utf-8">
<title>Revelation &amp; The Great Deception – Seminar Flyer</title>
<link rel="stylesheet" href="https://fonts.googleapis.com/css2?family=Baloo+2:wght@500;600;700&family=Open+Sans:ital,wght@0,400;0,600;0,700;1,400&display=swap">
<style>
  :root {
    --gold: #f5c400;
    --white: #f2f4f8;
    --night: #07080f;
    --deep: #101a3a;
    --pin: #d9b94a;
    --map-line: #c9c9cc;
  }
  * { margin: 0; padding: 0; box-sizing: border-box; }
  html, body { width: 1200px; height: 928px; overflow: hidden; background: var(--night); }
  .flyer {
    position: relative; width: 1200px; height: 928px; overflow: hidden;
    font-family: "Open Sans", Arial, sans-serif; color: var(--white);
  }
  .cover-art {
    position: absolute; inset: 0;
    background:
      radial-gradient(ellipse 220px 160px at 1140px 60px, rgba(230,220,240,.35), transparent 70%),
      radial-gradient(ellipse 260px 200px at 380px 560px, rgba(60,150,210,.5), transparent 70%),
      radial-gradient(ellipse 320px 240px at 430px 330px, rgba(110,90,170,.4), transparent 70%),
      radial-gradient(ellipse 360px 260px at 900px 420px, rgba(120,100,170,.3), transparent 70%),
      linear-gradient(180deg, rgba(0,0,0,0) 0%, rgba(0,0,0,0) 74%, rgba(0,0,0,.85) 88%, var(--night) 100%),
      linear-gradient(160deg, var(--deep) 0%, #1b2650 45%, #141a33 70%, var(--night) 100%);
  }
  .fold { position: absolute; left: 600px; top: 0; width: 1px; height: 928px; background: rgba(255,255,255,.05); }

  .back-panel { position: absolute; left: 0; top: 0; width: 600px; height: 928px; }
  .gold-head { font-family: "Baloo 2", "Trebuchet MS", sans-serif; color: var(--gold); font-weight: 500; }
  .invite { position: absolute; left: 72px; top: 66px; font-size: 19.5px; line-height: 27px; width: 445px; }
  .why-head { position: absolute; left: 72px; top: 150px; font-size: 19.5px; line-height: 26px; }
  .why-body { position: absolute; left: 72px; top: 176px; width: 452px; font-size: 15px; line-height: 22px; }
  .answers-head { position: absolute; left: 72px; top: 265px; font-size: 19.5px; line-height: 26px; }
  .questions { position: absolute; left: 72px; top: 294px; list-style: none; font-size: 15px; line-height: 21.8px; }
  .questions li { display: flex; align-items: center; gap: 8px; }
  .questions li::before { content: ""; width: 12px; height: 12px; border: 1.6px solid var(--gold); flex: none; }
  .submit-note { position: absolute; left: 77px; top: 448px; font-size: 15px; font-style: italic; }

  .location { position: absolute; left: 70px; top: 580px; font-size: 16px; line-height: 26.2px; font-style: normal; }
  .location .label { font-weight: 600; }
  .location .church { font-family: "Baloo 2", sans-serif; color: var(--gold); font-weight: 600; font-size: 18.5px; }
  .location strong { font-weight: 700; }
  .map-icon { position: absolute; left: 322px; top: 660px; width: 234px; height: 148px; }

  .perks { position: absolute; left: 0; width: 600px; text-align: center; font-size: 12.5px; }
  .perks.free { top: 855px; }
  .perks.stream { top: 881px; }
  .perks strong { font-weight: 700; }

  .front-panel { position: absolute; left: 600px; top: 0; width: 600px; height: 928px; }
  .dates { position: absolute; left: 77px; top: 82px; font-family: "Baloo 2", sans-serif; font-weight: 600; font-size: 25px; color: var(--gold); }
  .title { font-family: "Baloo 2", "Trebuchet MS", sans-serif; font-weight: 700; color: var(--gold); text-shadow: 0 3px 6px rgba(0,0,0,.45); }
  .title span { position: absolute; white-space: nowrap; line-height: 1; }
  .t-revelation { left: 78px; top: 183px; font-size: 94px; }
  .t-the { left: 78px; top: 308px; font-size: 50px; }
  .t-great { left: 229px; top: 272px; font-size: 94px; }
  .t-deception { left: 78px; top: 362px; font-size: 94px; }
  .presenter { position: absolute; right: 28px; top: 874px; font-size: 12.5px; }
  .presenter strong { font-weight: 700; }
</style>
</head>
<body>
<div class="flyer">
  <div class="cover-art" role="img" aria-label="Starry night sky with nebula clouds in deep blue and violet tones"></div>
  <div class="fold"></div>

  <section class="back-panel">
    <p class="invite gold-head">We invite you to come as you are. And discover hope &amp; lasting peace in these trouble times</p>

    <h2 class="why-head gold-head">Why Study Revelation?</h2>
    <p class="why-body">Blessed <em>is</em> he who reads and those who hear the words of this prophecy, and keep those things which are written in it; for the time <em>is</em> near. Revelation 1:3</p>

    <h2 class="answers-head gold-head">Find answers to your everyday questions:</h2>
    <ul class="questions">
      <li>What does the Bible say about the end of the world?</li>
      <li>Were there really Giants in the world?</li>
      <li>Are there UFO’s?</li>
      <li>Why is there so much pain and suffering in the world?</li>
      <li>Is there life after death?</li>
      <li>Is Heaven and Hell real?</li>
    </ul>
    <p class="submit-note">If you have a plaguing question, submit it and we will answer it.......</p>

    <address class="location">
      <div class="label">Meeting Location</div>
      <div class="church">Bethany Hill Church</div>
      <div>820 Meadow Ave., Brooklyn, NY 11230</div>
      <div>(corner of Meadow Ave &amp; Linden Rd)</div>
      <div>Phone: <strong>555-014-2121</strong></div>
      <div><strong>Dr. Marcus L. Reed, Pastor</strong></div>
      <div>Phone: <strong>555-019-6998</strong></div>
    </address>

    <svg class="map-icon" viewBox="0 0 234 148" aria-hidden="true">
      <g fill="none" stroke="var(--map-line)" stroke-width="6" stroke-linejoin="round">
        <path d="M6 140 L40 54 L110 64 L150 50 L214 58 L228 140 Z"/>
        <path d="M40 54 L70 140 M110 64 L120 140 M150 50 L170 140 M24 98 L222 100 M58 78 L92 92 L140 76 L200 82"/>
      </g>
      <path d="M161 2 a34 34 0 0 1 34 34 c0 22 -34 52 -34 52 s-34 -30 -34 -52 a34 34 0 0 1 34 -34 z" fill="var(--pin)"/>
      <circle cx="161" cy="35" r="16" fill="#eeeeee"/>
    </svg>

    <p class="perks free"><strong>FREE</strong> Admission | <strong>FREE</strong> Study Guides | <strong>FREE</strong> Books | <strong>FREE</strong> Health Materials</p>
    <p class="perks stream"><strong>Streaming live at:</strong> www.bethanyhill.org/watch-live</p>
  </section>

  <section class="front-panel">
    <p class="dates">May 19th - June 2nd, 2018</p>
    <h1 class="title">
      <span class="t-revelation">Revelation</span>
      <span class="t-the">&amp; The</span>
      <span class="t-great">Great</span>
      <span class="t-deception">Deception</span>
    </h1>
    <p class="presenter"><strong>Bethany Hill</strong> Presents</p>
  </section>
</div>
</body>
</html>
```